Need Flyer Design for real estate

Need a generic Flyer Design for real estate Company..

See few flyers attached for an ideas..need to have 4 directors pictures n contact details in one side (back side)..

Industry/Entity Type

Real Estate

Requirements
Must have
• Our Logo Colours..
• PANTONE 484 C ( RED)
• PANTONE 2766 C ( BLUE)

```html
<!DOCTYPE html>
<html lang="en">
<head>
<meta charset="utf-8">
<title>Meridian Real Estate Flyer</title>
<link href="https://fonts.googleapis.com/css2?family=Cinzel:wght@400;500&family=Great+Vibes&family=Raleway:wght@400;600;700&display=swap" rel="stylesheet">
<style>
  :root {
    --navy: #1b2462;
    --red: #c41230;
    --white: #ffffff;
    --ink: #2a2a2a;
    --page: #e4e4e4;
    --frame: rgba(255,255,255,0.45);
  }
  * { box-sizing: border-box; margin: 0; padding: 0; }
  html, body { width: 1200px; height: 1200px; overflow: hidden; }
  body { background: var(--page); font-family: 'Raleway', sans-serif; position: relative; }

  .flyer { position: absolute; left: 73px; width: 1061px; height: 499px; overflow: hidden; }
  .flyer--front { top: 61px; background: var(--navy); }
  .flyer--back { top: 633px; background: var(--white); }

  /* Front */
  .hero-photo {
    position: absolute; left: 0; top: 0; width: 618px; height: 499px;
    background: linear-gradient(120deg, #d9a67c 0%, #c9a99a 35%, #8d8fa5 70%, #d8d2cc 100%);
  }
  .room-tiles { position: absolute; left: 0; top: 0; width: 1061px; height: 499px; }
  .front-frame {
    position: absolute; left: 16px; top: 16px; right: 16px; bottom: 16px;
    border: 1px solid var(--frame); border-radius: 14px; pointer-events: none;
  }
  .welcome {
    position: absolute; left: 700px; width: 340px; top: 30px; text-align: center;
    font-family: 'Great Vibes', cursive; font-size: 96px; line-height: 1; color: var(--red);
  }
  .tagline {
    position: absolute; left: 700px; width: 340px; text-align: center;
    font-family: 'Cinzel', serif; line-height: 1;
  }
  .tagline--top { top: 155px; font-size: 30px; color: var(--white); letter-spacing: 1px; }
  .tagline--bottom { top: 196px; font-size: 44px; color: var(--red); letter-spacing: 1px; }

  .brand-block { position: absolute; text-align: center; color: var(--white); font-family: 'Cinzel', serif; }
  .brand {
    display: flex; align-items: center; justify-content: center; gap: 10px;
    font-weight: 400; white-space: nowrap; line-height: 1;
  }
  .brand-mark { width: 10px; height: 10px; background: var(--red); flex: none; }
  .brand-sub {
    display: flex; align-items: center; justify-content: center; gap: 8px;
    font-size: 10px; letter-spacing: 2px; line-height: 1; white-space: nowrap;
  }
  .brand-sub::before, .brand-sub::after { content: ""; height: 1px; width: 70px; background: rgba(255,255,255,0.7); }

  .brand-block--front { left: 710px; width: 320px; top: 386px; }
  .brand-block--front .brand { font-size: 38px; letter-spacing: 3px; }
  .brand-block--front .brand-sub { margin-top: 10px; }
  .website {
    position: absolute; left: 700px; width: 340px; top: 458px; text-align: center;
    font-family: 'Cinzel', serif; font-size: 14px; letter-spacing: 3px; color: var(--red);
  }

  /* Back */
  .back-glow {
    position: absolute; inset: 0 0 174px 0;
    background: linear-gradient(115deg, rgba(240,200,200,0.35) 0%, rgba(255,255,255,0) 30%, rgba(255,255,255,0) 70%, rgba(240,200,200,0.3) 100%);
  }
  .team-heading {
    position: absolute; top: 26px; left: 0; width: 100%; text-align: center;
    font-size: 23px; font-weight: 400; color: var(--navy); letter-spacing: 0.3px;
  }
  .team-member { position: absolute; top: 75px; width: 230px; text-align: center; }
  .team-member:nth-of-type(1) { left: 28px; }
  .team-member:nth-of-type(2) { left: 283px; }
  .team-member:nth-of-type(3) { left: 537px; }
  .team-member:nth-of-type(4) { left: 794px; }
  .portrait {
    width: 160px; height: 160px; margin: 0 auto; border-radius: 50%;
    border: 6px solid var(--navy);
    background: radial-gradient(circle at 50% 35%, #f2f2f2 0%, #d9d9de 55%, #3a4270 100%);
  }
  .member-name { margin-top: 18px; font-size: 13.5px; font-weight: 700; color: var(--red); }
  .member-detail { font-size: 11.5px; color: var(--ink); line-height: 1.3; }
  .team-divider { position: absolute; top: 95px; width: 1px; height: 136px; background: #9aa0b8; }

  .info-band {
    position: absolute; left: 0; bottom: 0; width: 100%; height: 174px; background: var(--navy);
  }
  .info-frame {
    position: absolute; left: 16px; right: 16px; top: 0; bottom: 16px;
    border: 1px solid var(--frame); border-top: none; border-radius: 0 0 14px 14px;
  }
  .info-divider { position: absolute; top: 16px; width: 1px; height: 142px; background: rgba(255,255,255,0.55); }
  .brand-block--back { left: 24px; width: 240px; top: 92px; }
  .brand-block--back .brand { font-size: 30px; letter-spacing: 2px; }
  .brand-block--back .brand-sub { margin-top: 8px; font-size: 8px; }
  .brand-block--back .brand-sub::before, .brand-block--back .brand-sub::after { width: 50px; }
  .about {
    position: absolute; left: 292px; top: 26px; width: 440px;
    font-size: 12.4px; line-height: 1.3; color: var(--white);
  }
  .about p + p { margin-top: 7px; }
  .contact { position: absolute; left: 805px; top: 16px; color: var(--white); }
  .contact-title { font-size: 17px; }
  .contact-title strong { color: var(--red); font-weight: 700; }
  .contact-rule { width: 30px; height: 2px; background: var(--red); margin: 6px 0 8px; }
  .contact-list { list-style: none; }
  .contact-list li { display: flex; align-items: center; gap: 10px; font-size: 17px; line-height: 25px; }
  .contact-list svg { width: 14px; height: 14px; flex: none; }
</style>
</head>
<body>

<section class="flyer flyer--front">
  <div class="hero-photo" role="img" aria-label="Happy couple moving into their new home, the woman sitting in a cardboard box"></div>
  <svg class="room-tiles" viewBox="0 0 1061 499">
    <defs>
      <linearGradient id="room-a" x1="0" y1="0" x2="1" y2="1"><stop offset="0" stop-color="#f3eee6"/><stop offset="1" stop-color="#c8bca8"/></linearGradient>
      <linearGradient id="room-b" x1="0" y1="0" x2="1" y2="1"><stop offset="0" stop-color="#e7e7ea"/><stop offset="1" stop-color="#6b6660"/></linearGradient>
      <linearGradient id="room-c" x1="0" y1="0" x2="1" y2="1"><stop offset="0" stop-color="#f0f0f0"/><stop offset="1" stop-color="#8a8a8a"/></linearGradient>
    </defs>
    <g role="img" aria-label="Bright living room interior">
      <rect x="564" y="43" width="108" height="108" rx="16" transform="rotate(45 618 97)" fill="url(#room-a)" stroke="#fff" stroke-width="4"/>
    </g>
    <g role="img" aria-label="Modern bedroom interior">
      <rect x="564" y="196" width="108" height="108" rx="16" transform="rotate(45 618 250)" fill="url(#room-b)" stroke="#fff" stroke-width="4"/>
    </g>
    <g role="img" aria-label="Lounge with grey sofa">
      <rect x="564" y="349" width="108" height="108" rx="16" transform="rotate(45 618 403)" fill="url(#room-c)" stroke="#fff" stroke-width="4"/>
    </g>
  </svg>
  <div class="front-frame"></div>
  <div class="welcome">Welcome</div>
  <div class="tagline tagline--top">ENTER WITH A</div>
  <div class="tagline tagline--bottom">HAPPY HEART</div>
  <div class="brand-block brand-block--front">
    <div class="brand"><span class="brand-mark"></span>MERIDIAN</div>
    <div class="brand-sub">REAL ESTATE</div>
  </div>
  <div class="website">WWW.YOURWEBSITE.COM</div>
</section>

<section class="flyer flyer--back">
  <div class="back-glow"></div>
  <h2 class="team-heading">LOREM IPSUM IS SIMPLY DUMMY TEXT</h2>

  <div class="team-member">
    <div class="portrait" role="img" aria-label="Portrait of director one"></div>
    <div class="member-name">NAME GOES HERE</div>
    <div class="member-detail">Designation<br>+0123 456 789<br>info@yourmailid.com</div>
  </div>
  <div class="team-member">
    <div class="portrait" role="img" aria-label="Portrait of director two"></div>
    <div class="member-name">NAME GOES HERE</div>
    <div class="member-detail">Designation<br>+0123 456 789<br>info@yourmailid.com</div>
  </div>
  <div class="team-member">
    <div class="portrait" role="img" aria-label="Portrait of director three"></div>
    <div class="member-name">NAME GOES HERE</div>
    <div class="member-detail">Designation<br>+0123 456 789<br>info@yourmailid.com</div>
  </div>
  <div class="team-member">
    <div class="portrait" role="img" aria-label="Portrait of director four"></div>
    <div class="member-name">NAME GOES HERE</div>
    <div class="member-detail">Designation<br>+0123 456 789<br>info@yourmailid.com</div>
  </div>
  <div class="team-divider" style="left:271px"></div>
  <div class="team-divider" style="left:526px"></div>
  <div class="team-divider" style="left:782px"></div>

  <div class="info-band">
    <div class="info-frame"></div>
    <div class="info-divider" style="left:271px"></div>
    <div class="info-divider" style="left:747px"></div>
    <div class="brand-block brand-block--back">
      <div class="brand"><span class="brand-mark"></span>MERIDIAN</div>
      <div class="brand-sub">REAL ESTATE</div>
    </div>
    <div class="about">
      <p>Lorem Ipsum is simply dummy text of the printing and typesetting industry. Lorem Ipsum has been the industry's standard dummy text ever since the 1500s, when an unknown printer took a galley of type and scrambled it to make a type specimen book.</p>
      <p>It has survived not only five centuries, but also the leap into electronic type-setting, remaining essentially unchanged. It has survived not only five cen-turies, but also the leap into electronic typesetting.</p>
    </div>
    <div class="contact">
      <div class="contact-title"><strong>Get In Touch</strong> With Us :</div>
      <div class="contact-rule"></div>
      <ul class="contact-list">
        <li><svg viewBox="0 0 14 14"><circle cx="7" cy="7" r="7" fill="#c41230"/><path d="M7 3a2.5 2.5 0 0 0-2.5 2.5C4.5 7.5 7 11 7 11s2.5-3.5 2.5-5.5A2.5 2.5 0 0 0 7 3z" fill="#fff"/><circle cx="7" cy="5.5" r="1" fill="#c41230"/></svg>Address goes Here</li>
        <li><svg viewBox="0 0 14 14"><circle cx="7" cy="7" r="7" fill="#c41230"/><path d="M4.5 3.5l1.5 0 .6 2-1 .8a5 5 0 0 0 2.1 2.1l.8-1 2 .6 0 1.5c-3.5.3-6.3-2.5-6-6z" fill="#fff"/></svg>+0123 456 789</li>
        <li><svg viewBox="0 0 14 14"><circle cx="7" cy="7" r="7" fill="#c41230"/><rect x="3.5" y="4.5" width="7" height="5" fill="#fff"/><path d="M3.5 4.5L7 7.3l3.5-2.8" fill="none" stroke="#c41230" stroke-width="0.8"/></svg>info@yourmailid.com</li>
        <li><svg viewBox="0 0 14 14"><circle cx="7" cy="7" r="7" fill="#c41230"/><circle cx="7" cy="7" r="3.8" fill="none" stroke="#fff" stroke-width="0.9"/><ellipse cx="7" cy="7" rx="1.6" ry="3.8" fill="none" stroke="#fff" stroke-width="0.9"/><path d="M3.2 7h7.6" stroke="#fff" stroke-width="0.9"/></svg>www.yourwebsite.com</li>
      </ul>
    </div>
  </div>
</section>

</body>
</html>
```